Contact card for an aggressive entrepreneur

I am looking for a business/contact card as an individual. I operate under the company name The Varden Collective, LLC (but don't generally use that other than for billing). I have explored a few ideas and am now turning to artplaza to connect with people more creative than me. I am trying to capture a diverse set of passions, which I will summarize with the following keywords (which may or may not be ON the card and are in no particular order):

entrepreneur
shark diver
MBA
visionary
defenseman
marketing guru
hockey coach
teacher
reader
writer
cook
captain
scuba diver
beach bum
Type A
Brightwater
Vermont
New York
Montauk
founder
leader
focused
driven
teammate father

hope that makes some sense!
Updates

Please note the photo is for reference - unless there is a really creative way to use it I do not need a card with a head shot (I am not a model or an actor!)

Project Deadline Extended
Reason: There have been several requests to submit designs so we will close this project this Wednesday and select a design by this Friday. Thank you to all for your great ideas and submissions!

I am reviewing the designs and will select one by end of day tomorrow, Tuesday, EST
Thank you to all who participated!

Target Market(s)

everyone from business contacts to personal acquaintances

Industry/Entity Type

Business

Requirements
Must have
• Must be utterly original, extraordinary and memorable.
How it achieves that is up to you!
Essential contact information that needs to be included:

phone: (555) 374-1926
email: tomas@vardencollective.example
chat: tomas.varden
Nice to have
• A striking visual whether that is a photo or illustration
Some way of conveying the diversity of what I am and what I do
Feel free to use the printing or physical material of the card to make it stand out.
Should not have
• I am not into "logos" but that being said I do not want to limit creativity in any way so feel free to ignore any part of this brief if you disagree with me. No need to use the attached photo of me, but that's what I look like.

```html
<!DOCTYPE html>
<html lang="en">
<head>
<meta charset="utf-8">
<title>The Varden Collective — Contact Card</title>
<link rel="stylesheet" href="https://fonts.googleapis.com/css2?family=Poppins:wght@300;500;700&display=swap">
<style>
  :root {
    --board: #a0b0ae;
    --card: #ffffff;
    --texture: #e6e6e6;
    --red: #d4000f;
    --label-ink: #1a1a1a;
  }
  * { box-sizing: border-box; margin: 0; padding: 0; }
  html, body { width: 982px; height: 1200px; overflow: hidden; }
  body {
    background: var(--board);
    position: relative;
    font-family: "Poppins", Arial, sans-serif;
  }
  .side-label {
    position: absolute;
    left: 0;
    width: 490px;
    height: 35px;
    background: linear-gradient(90deg, #fff 0%, #fff 62%, rgba(255,255,255,0) 100%);
    font-weight: 700;
    font-size: 24px;
    letter-spacing: 5px;
    color: var(--label-ink);
    line-height: 35px;
    padding-left: 104px;
  }
  .side-label--front { top: 37px; }
  .side-label--back { top: 1122px; }

  .card {
    position: absolute;
    left: 106px;
    width: 766px;
    height: 439px;
    background: var(--card);
    overflow: hidden;
  }
  .card--front { top: 136px; }
  .card--back { top: 618px; }

  .word-field {
    position: absolute;
    left: 0;
    top: 4px;
    width: 100%;
    color: var(--texture);
    font-size: 29px;
    font-weight: 300;
    line-height: 31px;
    white-space: nowrap;
    user-select: none;
  }
  .word-row {
    display: flex;
    justify-content: space-between;
    height: 31px;
  }
  .word-row--heavy { font-weight: 500; }
  .word-row--open { letter-spacing: 4px; }
  .strong { font-weight: 700; }

  .company-name {
    position: absolute;
    left: 30px;
    top: 218px;
    color: var(--red);
    font-weight: 700;
    font-size: 100px;
    line-height: 1;
    letter-spacing: -2px;
  }

  .contact {
    position: absolute;
    left: 0;
    width: 100%;
    text-align: center;
    color: var(--red);
    line-height: 31px;
    height: 31px;
  }
  .contact--phone {
    top: 66px;
    font-weight: 700;
    font-size: 30px;
    letter-spacing: 6px;
  }
  .contact--email {
    top: 159px;
    font-family: Arial, Helvetica, sans-serif;
    font-size: 29px;
  }
  .contact--chat {
    top: 283px;
    font-weight: 700;
    font-size: 29px;
    letter-spacing: 4px;
  }
</style>
</head>
<body>
  <div class="side-label side-label--front">Front</div>

  <section class="card card--front">
    <div class="word-field" aria-hidden="true">
      <div class="word-row word-row--heavy word-row--open"><span>innovator</span><span>deep</span><span>swimmer</span></div>
      <div class="word-row"><span>strategist</span><span class="strong">mentor</span><span>skater</span><span>planner</span></div>
      <div class="word-row word-row--open"><span>sailor</span><span>runner</span><span class="strong">builder</span></div>
      <div class="word-row"><span class="strong">thinker</span><span>traveler</span><span>angler</span><span>skier</span></div>
      <div class="word-row word-row--open"><span>optimist</span><span class="strong">climber</span><span>chef</span></div>
      <div class="word-row"><span>Brightwater</span><span>harbor</span><span class="strong">pioneer</span><span>tide</span></div>
    </div>
    <h1 class="company-name">The Varden<br>Collective, LLC</h1>
  </section>

  <section class="card card--back">
    <div class="word-field" aria-hidden="true">
      <div class="word-row word-row--heavy word-row--open"><span>innovator</span><span>deep</span><span>swimmer</span></div>
      <div class="word-row"><span>strategist</span><span class="strong">mentor</span><span>skater</span><span>planner</span></div>
      <div class="word-row word-row--open"><span>sailor</span><span class="strong">builder</span></div>
      <div class="word-row"><span class="strong">thinker</span><span>traveler</span><span>angler</span><span>skier</span></div>
      <div class="word-row word-row--open"><span>optimist</span><span class="strong">climber</span><span>chef</span></div>
      <div class="word-row"><span>harbor</span><span>tide</span></div>
      <div class="word-row"><span>Brightwater</span><span class="strong">pioneer</span><span>starter</span></div>
      <div class="word-row word-row--open"><span>partner</span><span>parent</span><span class="strong">rider</span></div>
      <div class="word-row word-row--heavy word-row--open"><span>innovator</span><span>deep</span><span>swimmer</span></div>
      <div class="word-row"><span>mentor</span><span>skater</span></div>
      <div class="word-row word-row--open"><span>sailor</span><span>runner</span><span class="strong">builder</span></div>
      <div class="word-row"><span class="strong">thinker</span><span>traveler</span><span>angler</span><span>skier</span></div>
      <div class="word-row word-row--open"><span>optimist</span><span class="strong">climber</span><span>chef</span></div>
      <div class="word-row"><span>Brightwater</span><span>harbor</span><span class="strong">pioneer</span><span>tide</span></div>
    </div>
    <p class="contact contact--phone">(555) 374-1926</p>
    <p class="contact contact--email">tomas@vardencollective.example</p>
    <p class="contact contact--chat">chat: tomas.varden</p>
  </section>

  <div class="side-label side-label--back">Back</div>
</body>
</html>
```